Stationery wanted for Brand New Law Firm

I need a stationery for a law firm that I am establishing. I am after letterhead (black & white and colour version, envelope, document folder, business cards and email signature
The firm will be a "modern" law firm providing commercial advice and transactional assistance to small to medium businesses (sales, purchases and leases of commercial property, business structuring advice, shareholders agreement etc).

Target Market(s)

Small to medium business owners in Sydney, Australia

Industry/Entity Type

Legal

Contact Information for Business Card

Rosalind Penhale
Principal Lawyer
Penhale Legal
PO Box 4382 Kelmore Arcade NSW 2210
[Phone No to be provided]
r@penhalelegal.com.au
www.penhalelegal.com.au
Tag line - "Expert legal advice for property and business owners"

Colors
ffffff
0555a3
ffc214

Requirements
Must have
• * Attached logo
* Letterhead have colour and black and white options. Other documents to be the same colour scheme as the attached logo.
* Modern, minimalistic feel
* Letterhead and email signature must include the following words:
"Liability limited by a scheme approved under Professional Standards Legislation."

```html
<!DOCTYPE html>
<html lang="en">
<head>
<meta charset="utf-8">
<title>Penhale Legal Stationery</title>
<link rel="stylesheet" href="https://fonts.googleapis.com/css2?family=Lato:wght@400;700&family=Pinyon+Script&display=swap">
<style>
:root{
  --navy:#151a4f;
  --gold:#d0a043;
  --paper:#f3f3f3;
  --ink:#3d3d3d;
  --muted:#5a5a5a;
  --bg:#ebebeb;
  --rule:#b9b9b9;
}
*{margin:0;padding:0;box-sizing:border-box}
html,body{width:1200px;height:1019px;overflow:hidden}
body{background:var(--bg);font-family:'Lato',sans-serif;color:var(--ink);position:relative}
.piece{position:absolute;background:var(--paper);overflow:hidden}
.band{position:absolute;left:0;right:0;bottom:0}
.wordmark{position:absolute;font-family:'Lato',sans-serif;font-weight:400;color:var(--navy);white-space:nowrap;letter-spacing:.02em}
.wordmark.light{color:#fff}
.liability{font-size:7.4px;line-height:1.25;color:var(--muted)}
.liability b{font-weight:700;color:#444}
.icon{display:inline-block;width:6px;height:6px;vertical-align:-0.5px;margin-right:3px}

/* Letterhead */
.letterhead{left:157px;top:151px;width:437px;height:617px}
.letterhead .wordmark{left:33px;top:24px;font-size:22px}
.letter{position:absolute;left:46px;top:146px;width:344px;font-size:7.4px;line-height:10.3px;color:var(--ink)}
.letter .recipient{margin-top:12px}
.letter .recipient b{color:#222}
.letter .salutation{margin-top:20px}
.letter p.body{margin-top:10px;text-align:justify}
.letter .closing{margin-top:30px}
.letter .signature{font-family:'Pinyon Script',cursive;font-size:15px;line-height:20px;color:#2a2a2a;margin:4px 0 0 4px}
.letter-footer{position:absolute;left:35px;top:542px;font-size:7.4px;line-height:9px;color:var(--muted)}
.letter-footer .contacts{margin-top:3px}
.letterhead .liability{position:absolute;right:39px;top:583px;text-align:right}
.letterhead .band{height:6px;background:linear-gradient(100deg,var(--navy) 50%,var(--gold) 50%)}

/* Business card front */
.card-front{left:625px;top:139px;width:228px;height:130px}
.card-front .wordmark{left:0;right:0;top:22px;text-align:center;font-size:14px}
.card-front .holder{position:absolute;right:125px;top:75px;text-align:right}
.card-front .holder h2{font-size:7px;font-weight:700;color:var(--navy)}
.card-front .holder span{font-size:5px;color:var(--muted)}
.card-front .divider{position:absolute;left:114px;top:65px;width:1px;height:32px;background:var(--rule)}
.card-front .details{position:absolute;left:126px;top:65px;font-size:5px;line-height:6.3px;color:var(--muted)}
.card-front .details .contacts{margin-top:3px}
.card-front .tagline{position:absolute;left:0;right:0;top:112px;text-align:center;font-size:5px;color:var(--muted)}
.card-front .tagline b{color:#444}
.card-front .band{height:5px;background:linear-gradient(100deg,var(--navy) 50%,var(--gold) 50%)}

/* Business card back */
.card-back{left:897px;top:139px;width:227px;height:130px;background:var(--navy)}
.card-back .wordmark{left:0;right:0;top:48px;text-align:center;font-size:18px}
.card-back .liability{position:absolute;left:0;right:0;top:104px;text-align:center;font-size:5px;line-height:6.5px;color:#e6e6f0}
.card-back .liability b{color:#fff}

/* Envelope front */
.envelope-front{left:624px;top:297px;width:501px;height:217px}
.envelope-front .wordmark{left:43px;top:32px;font-size:17px}
.envelope-front .return{position:absolute;left:43px;top:80px;font-size:7.4px;line-height:9px;color:var(--muted)}
.envelope-front .liability{position:absolute;left:43px;top:177px}
.envelope-front .window{position:absolute;left:301px;top:143px;width:145px;height:50px;border-radius:6px;border:1px solid #c9c9c9;background:linear-gradient(100deg,#cfcfcf,#f4f4f4 55%,#d4d4d4)}
.envelope-front .band{height:8px;background:linear-gradient(100deg,var(--gold) 9%,var(--navy) 9%)}

/* Envelope back */
.envelope-back{left:624px;top:550px;width:501px;height:218px;background:var(--paper)}
.envelope-back .flap{position:absolute;left:0;top:0;width:501px;height:72px}
.envelope-back .wordmark{left:0;right:0;top:25px;text-align:center;font-size:14px}
.envelope-back .web{position:absolute;left:0;right:0;top:190px;text-align:center;font-size:7.4px;color:var(--muted)}
.envelope-back .web b{color:#444}

/* Email signature */
.email-signature{left:398px;top:793px;width:404px;height:130px}
.email-signature .wordmark{left:18px;top:44px;font-size:17px}
.email-signature .social{position:absolute;left:56px;top:89px;display:flex;gap:3px}
.email-signature .social span{width:11px;height:11px;border-radius:50%;background:var(--navy)}
.email-signature .holder{position:absolute;left:172px;top:22px}
.email-signature .holder h2{font-size:10px;font-weight:700;color:var(--navy);line-height:12px}
.email-signature .holder span{font-size:7.4px;color:var(--muted)}
.email-signature .contacts{position:absolute;left:172px;top:55px;font-size:7.4px;line-height:9px;color:var(--muted)}
.email-signature .address{position:absolute;left:280px;top:55px;font-size:7.4px;line-height:9px;color:var(--muted)}
.email-signature .rule{position:absolute;left:172px;top:83px;width:199px;height:1px;background:var(--rule)}
.email-signature .liability{position:absolute;left:172px;top:92px}
.email-signature .band{height:6px;background:linear-gradient(100deg,var(--navy) 50%,var(--gold) 50%)}
</style>
</head>
<body>

<svg width="0" height="0" style="position:absolute" aria-hidden="true">
  <symbol id="i-phone" viewBox="0 0 10 10"><path d="M2 1l2 0 1 2.5-1.2 1a6 6 0 0 0 2.7 2.7l1-1.2L10 7v2c0 .6-.4 1-1 1A9 9 0 0 1 0 1c0-.6.4-1 1-1z" fill="#151a4f"/></symbol>
  <symbol id="i-mail" viewBox="0 0 10 8"><rect x="0" y="0" width="10" height="8" rx="1" fill="#151a4f"/><path d="M.5 1l4.5 3.5L9.5 1" stroke="#fff" stroke-width="1" fill="none"/></symbol>
  <symbol id="i-web" viewBox="0 0 10 10"><circle cx="5" cy="5" r="4.4" fill="none" stroke="#151a4f" stroke-width="1.2"/><path d="M.6 5h8.8M5 .6c-2.4 2.6-2.4 6.2 0 8.8M5 .6c2.4 2.6 2.4 6.2 0 8.8" stroke="#151a4f" stroke-width=".9" fill="none"/></symbol>
</svg>

<section class="piece letterhead">
  <div class="wordmark">Penhale Legal</div>
  <div class="letter">
    <div class="date">01 January 2050</div>
    <div class="recipient"><b>Company (Pvt) Ltd.</b><br>PO Box 2210 Fernlea St<br>Sample City Country 2210</div>
    <div class="salutation">Dear Daniel Marsh,</div>
    <p class="body">Lorem ipsum dolor sit amet, consectetuer adipiscing elit, sed diam nonummy nibh euismod tincidunt ut laoreet dolore magna aliquam erat volutpat. Ut wisi enim ad minim veniam, quis nostrud exerci tation ullamcorper suscipit lobortis nisl ut aliquip ex ea commodo consequat. Duis dolore te feugait nulla facilisi. Nam liber tempor cum soluta nobis eleifend option congue nihil imperdiet doming id quod mazim placerat facer possim assum. Lorem ipsum dolor sit amet, consectetuer adipiscing elit, sed diam nonummy nibh euismod tincidunt ut laoreet dolore magna aliquam erat volutpat. Ut wisi enim ad minim veniam, quis nostrud exerci tation ullamcorper suscipit lobortis nisl ut aliquip ex ea commodo consequat.</p>
    <p class="body">Consectetuer adipiscing elit, sed diam nonummy nibh euismod tincidunt ut laoreet dolore magna aliquam erat volutpat. Ut wisi enim ad minim veniam, quis nostrud exerci tation ullamcorper suscipit lobortis nisl ut aliquip ex ea commodo consequat. Consectetuer adipiscing elit, sed diam nonummy nibh euismod tincidunt ut laoreet dolore magna aliquam erat volutpat. Ut wisi enim ad minim veniam, quis nostrud exerci tation ullamcorper suscipit lobortis nisl ut aliquip ex ea commodo consequat.</p>
    <p class="body">Consectetuer adipiscing elit, sed diam nonummy nibh euismod tincidunt ut laoreet dolore magna aliquam erat volutpat. Ut wisi enim ad minim veniam, quis nostrud exerci tation ullamcorper suscipit lobortis nisl ut aliquip ex ea commodo consequat. Consectetuer adipiscing elit, sed diam nonummy nibh euismod tincidunt ut laoreet dolore magna aliquam erat volutpat. Ut wisi enim ad minim veniam, quis nostrud exerci tation ullamcorper suscipit lobortis nisl ut aliquip ex ea commodo consequat.</p>
    <div class="closing">Sincerely Yours</div>
    <div class="signature">Thomas Edward Calder</div>
  </div>
  <div class="letter-footer">
    Penhale Legal LLC<br>PO Box 4382 Kelmore Arcade<br>NSW 2210
    <div class="contacts">
      <svg class="icon"><use href="#i-phone"/></svg>(200) 555.0142<br>
      <svg class="icon"><use href="#i-mail"/></svg>r@penhalelegal.com.au<br>
      <svg class="icon"><use href="#i-web"/></svg>www.penhalelegal.com.au
    </div>
  </div>
  <div class="liability">Liability limited by a scheme approved under<br><b>Professional Standards Legislation</b>.</div>
  <div class="band"></div>
</section>

<section class="piece card-front">
  <div class="wordmark">Penhale Legal</div>
  <div class="holder"><h2>Rosalind Penhale</h2><span>Principal Lawyer | Penhale Legal</span></div>
  <div class="divider"></div>
  <div class="details">
    PO Box 4382 Kelmore Arcade<br>NSW 2210
    <div class="contacts">
      <svg class="icon" style="width:4px;height:4px"><use href="#i-phone"/></svg>(200) 555.0142<br>
      <svg class="icon" style="width:4px;height:4px"><use href="#i-mail"/></svg>r@penhalelegal.com.au<br>
      <svg class="icon" style="width:4px;height:4px"><use href="#i-web"/></svg>www.penhalelegal.com.au
    </div>
  </div>
  <div class="tagline">Expert Legal Advice for <b>Property &amp; Business Owners</b></div>
  <div class="band"></div>
</section>

<section class="piece card-back">
  <div class="wordmark light">Penhale Legal</div>
  <div class="liability">Liability limited by a scheme approved under<br><b>Professional Standards Legislation</b></div>
</section>

<section class="piece envelope-front">
  <div class="wordmark">Penhale Legal</div>
  <div class="return">Penhale Legal LLC<br>PO Box 4382 Kelmore Arcade<br>NSW 2210</div>
  <div class="liability">Liability limited by a scheme approved under<br><b>Professional Standards Legislation</b>.</div>
  <div class="window"></div>
  <div class="band"></div>
</section>

<section class="piece envelope-back">
  <svg class="flap" viewBox="0 0 501 72" preserveAspectRatio="none" aria-hidden="true">
    <defs>
      <linearGradient id="flapShade" x1="0" x2="1" y1="0" y2="0">
        <stop offset="0" stop-color="#151a4f"/>
        <stop offset=".65" stop-color="#151a4f"/>
        <stop offset=".85" stop-color="#232a78"/>
        <stop offset="1" stop-color="#151a4f"/>
      </linearGradient>
    </defs>
    <path d="M0 0H501L484 56Q480 71 465 71H36Q21 71 17 56Z" fill="url(#flapShade)"/>
  </svg>
  <div class="wordmark light">Penhale Legal</div>
  <div class="web">www.<b>penhalelegal</b>.com.au</div>
</section>

<section class="piece email-signature">
  <div class="wordmark">Penhale Legal</div>
  <div class="social" aria-label="Social links"><span></span><span></span><span></span><span></span></div>
  <div class="holder"><h2>Rosalind Penhale</h2><span>Principal Lawyer | Penhale Legal</span></div>
  <div class="contacts">
    <svg class="icon"><use href="#i-phone"/></svg>(200) 555.0142<br>
    <svg class="icon"><use href="#i-mail"/></svg>r@penhalelegal.com.au<br>
    <svg class="icon"><use href="#i-web"/></svg>www.penhalelegal.com.au
  </div>
  <div class="address">Penhale Legal LLC<br>PO Box 4382 Kelmore Arcade<br>NSW 2210</div>
  <div class="rule"></div>
  <div class="liability">Liability limited by a scheme approved under<br><b>Professional Standards Legislation</b>.</div>
  <div class="band"></div>
</section>

</body>
</html>
```